The Marisol & Jocelyn Fruit Co.

We produce a very high quality freeze dried fruit, all organic, no preservative, no additives, nothing but the fruit. To get more use out of a facility we have in Charlotte, we decided to pursue some high end online retailers with a high end freeze dried organic fruit. We are looking for a very high end, upper east side, trendy, hip, logo and package design for this. There are 4 SKU's - Freeze Dried Strawberries, Freeze Dried Blueberries, Freeze Dried Cherries, and a blend of of all 3 as the 4th SKU. 2 labels each that are 6" x 6" - The front, again needs to be fun and trendy big bold etc. Nothing frilly and Quiet Barn by the creek. The back needs to contain the nutritional statements for each and some copy describing the product and the company.
Updates
This would be one of only a few competitors in this segment
We are looking to steal a page from the wine industry. The coolest looking label on the shelf wins over the uneducated wine buyer. The designs are all fine, but they need to be sleeker, sexier, funner, etc. Someone should look at the label and say....wow that is FUN AND SEXY! I have to buy some! VORBEX.COM screams that. Don't worry so much about pictures of the fruit as the bag is going to be clear. Sell the brand not the fruit. OK?
Reason: Why not?
Reason: Final Selection by Monday 5pm EST.
For all designs that have not been eliminated:
Reason: Final selections. All four designs front and back on one file uploaded by noon tomorrow ( 12:01 PM EST New York)
Target Market(s)
People that would shop at sites like www.vorbex.com
Industry/Entity Type
It Company
Requirements
Nice to have
- The brand is named after our two daughters - One is very girly and the other is very "sassy" It would be fun to have the logo capture their personalities a little. I have uploaded a picture. Marisol on the left, Jocelyn on the right.
Also, another of our brands, Hank Pellow, packaging is attached here. Some consistency in look and feel may be good.
Should not have
- Nothing frilly or dainty, or delicate. Colorful fun and bold but trendy.

```html
<!DOCTYPE html>
<html lang="en">
<head>
<meta charset="utf-8">
<title>Marisol &amp; Jocelyn – Freeze Dried Strawberries Label</title>
<link rel="stylesheet" href="https://fonts.googleapis.com/css2?family=Amatic+SC:wght@400;700&family=Sofia&display=swap">
<style>
  :root {
    --label-green: #9dbb51;
    --band-green: #b4cc7c;
    --band-line: #c9dba0;
    --text-white: #ffffff;
    --berry-red: #c8321f;
    --berry-deep: #a5261a;
  }
  * { margin: 0; padding: 0; box-sizing: border-box; }
  html, body {
    width: 1200px;
    height: 1200px;
    overflow: hidden;
    background: var(--label-green);
  }
  .label {
    position: relative;
    width: 1200px;
    height: 1200px;
    background: var(--label-green);
    color: var(--text-white);
    font-family: "Amatic SC", cursive;
    text-align: center;
  }
  .brand-name {
    position: absolute;
    top: 88px;
    left: 0;
    width: 100%;
    font-family: "Amatic SC", cursive;
    font-weight: 700;
    font-size: 170px;
    line-height: 1;
    letter-spacing: 4px;
    color: var(--text-white);
  }
  .fruit-art {
    position: absolute;
    top: 345px;
    left: 270px;
    width: 690px;
    height: 370px;
    border-radius: 180px;
    background: radial-gradient(ellipse at center, var(--berry-red) 0%, var(--berry-deep) 100%);
  }
  .net-weight {
    position: absolute;
    top: 732px;
    left: 0;
    width: 100%;
    font-size: 36px;
    font-weight: 700;
  }
  .product-band {
    position: absolute;
    top: 806px;
    left: 0;
    width: 100%;
    height: 148px;
    border-top: 5px solid var(--band-line);
    border-bottom: 5px solid var(--band-line);
  }
  .product-band-fill {
    position: absolute;
    top: 26px;
    left: 0;
    width: 100%;
    height: 86px;
    background: var(--band-green);
  }
  .product-name {
    position: absolute;
    top: 0;
    left: 0;
    width: 100%;
    height: 100%;
    display: flex;
    align-items: center;
    justify-content: center;
    gap: 22px;
    white-space: nowrap;
  }
  .product-type {
    font-family: "Amatic SC", cursive;
    font-weight: 700;
    font-size: 84px;
    letter-spacing: 2px;
  }
  .product-fruit {
    font-family: "Sofia", cursive;
    font-size: 72px;
  }
  .claims {
    position: absolute;
    top: 1018px;
    left: 0;
    width: 100%;
    list-style: none;
    font-size: 40px;
    font-weight: 700;
    line-height: 48px;
    letter-spacing: 1px;
  }
</style>
</head>
<body>
  <main class="label">
    <h1 class="brand-name">Marisol &amp; Jocelyn</h1>

    <div class="fruit-art" role="img" aria-label="Illustration of three red strawberries with green leaves"></div>

    <p class="net-weight">1 oz</p>

    <div class="product-band">
      <div class="product-band-fill"></div>
      <h2 class="product-name">
        <span class="product-type">Freeze Dried</span>
        <span class="product-fruit">Strawberries</span>
      </h2>
    </div>

    <ul class="claims">
      <li>100% Organic</li>
      <li>No Preservatives</li>
      <li>No Sugar Added</li>
    </ul>
  </main>
</body>
</html>
```